Interior designer needs business card design

I need a card for my new interior design company. I de sign mostly kitchens and baths, but don't want the card to list and specialty. I've gotten several clients already by Dordrecht of mouth, but now need to begin advertising.
I've got a pic of a silk screen used to print my father's old real estate sign and was hoping to use it as the basis for my card design.
Instead of "Sold by Marivone", I'd like the front of my card to read "Design by Marivone".
I like the font styles and banner and would like to stay as close to the original as possible, but with some twist--maybe color, not sure. Surprise me!
The back should list my email and phone
marivonedesign@quillpost.example
225-555-0193

```html
<!DOCTYPE html>
<html lang="en">
<head>
<meta charset="utf-8">
<title>Marivone Interior Design – Business Card</title>
<link rel="stylesheet" href="https://fonts.googleapis.com/css2?family=Open+Sans:wght@300;700;800&display=swap">
<style>
  :root {
    --backdrop: #e9e6e1;
    --card-light: #ffffff;
    --card-dark: #111111;
    --ink: #0d0d0d;
    --ink-soft: #3a3a3a;
    --paper: #ffffff;
    --mark-on-dark: #2c2c2c;
  }
  * { box-sizing: border-box; margin: 0; padding: 0; }
  html, body {
    width: 1200px;
    height: 844px;
    overflow: hidden;
    background: var(--backdrop);
    font-family: "Open Sans", sans-serif;
  }
  .canvas {
    width: 1200px;
    height: 844px;
    display: flex;
    align-items: center;
    justify-content: center;
    gap: 80px;
  }
  .card {
    width: 380px;
    height: 620px;
    border-radius: 22px;
    box-shadow: 0 10px 30px rgba(0,0,0,.18);
    display: flex;
    flex-direction: column;
    align-items: center;
  }
  .card--front {
    background: var(--card-light);
    color: var(--ink);
    padding: 70px 30px 40px;
  }
  .card--back {
    background: var(--card-dark);
    justify-content: center;
  }
  .wordmark {
    font-weight: 800;
    text-transform: uppercase;
    text-align: center;
    line-height: 1.05;
    letter-spacing: 1px;
  }
  .wordmark__line { display: block; font-size: 58px; }
  .wordmark__by { display: block; font-size: 16px; letter-spacing: 2px; margin: 4px 0; }
  .wordmark__name { display: block; font-size: 52px; }
  .card--front .wordmark { color: var(--ink); }
  .card--back .wordmark { color: var(--mark-on-dark); }
  .details {
    margin-top: auto;
    width: 100%;
    text-align: center;
  }
  .details__name {
    font-weight: 800;
    font-size: 27px;
    letter-spacing: 1px;
    text-transform: uppercase;
  }
  .details__role {
    font-weight: 300;
    font-size: 22px;
    letter-spacing: 2px;
    color: var(--ink-soft);
    text-transform: uppercase;
    margin-top: 2px;
  }
  .details__phone-band {
    margin: 14px -6px 12px;
    background: var(--ink);
    color: var(--paper);
    font-weight: 700;
    font-size: 32px;
    letter-spacing: 2px;
    padding: 6px 0;
    clip-path: polygon(0 0, 100% 0, 96% 50%, 100% 100%, 0 100%, 4% 50%);
  }
  .details__email {
    font-weight: 700;
    font-size: 17px;
  }
</style>
</head>
<body>
  <main class="canvas">
    <article class="card card--front">
      <h1 class="wordmark">
        <span class="wordmark__line">Design</span>
        <span class="wordmark__by">by</span>
        <span class="wordmark__name">Marivone</span>
      </h1>
      <section class="details">
        <p class="details__name">Name Marivone</p>
        <p class="details__role">Interior Designer</p>
        <p class="details__phone-band">225-555-0193</p>
        <p class="details__email">marivonedesign@quillpost.example</p>
      </section>
    </article>
    <article class="card card--back">
      <p class="wordmark">
        <span class="wordmark__line">Design</span>
        <span class="wordmark__by">by</span>
        <span class="wordmark__name">Marivone</span>
      </p>
    </article>
  </main>
</body>
</html>
```